Freelance film producer/editor wants you to gleam nova!

'Gleam Nova' is my production business based in Melbourne, though I do a fair bit of work overseas. I'm a one woman show most of the time but enlist other crew members for larger projects. I manage productions from start to finish including producing, filming, editing, distribution, photography and animation.

My current tag line and details are as follows:

Petra Vandoren
Producer. Editor. Thinker.
[M] +61 492 157 630
[E] pv[at]brightpanel.com.au
www.brightpanel.com.au

I have a fairly wicked sense of humour and love a good pun, so feel free to work this into your design!

The final designs should demonstrate the areas I work in but not limited to. I'd rather not use old and typical "film" looking elements such as a clapper or negative reel. Having said that, the logo itself (attached) is quite typical because the first 'o' is a closed aperture and the second is a wide aperture. Happy for the logo to be pulled apart for the business card to be more interesting.

The majority of projects I work on are quite different and in some cases a bit crazy. Lots of travel involved. The main difference between me and other producers is that I don't say I work in 'film', even though i do. I want the card to leave me open to new roles and projects as opposed to squashing myself into one particular category.

I'm open to colour but prefer a simple design that isn't too hectic.

I have also attached an example I did like that was printed on plastic but then I realised so many other people had ripped it off....

I'm open to paper board or plastic (transparent) designs etc. One sided or two sided.

Thanks for sharing your ideas with me and please, go as nuts as you want to with this! :)

Target Market(s)

My clients range from non profits in health and educational institutions to record labels and well known artists. The business attracts corporates as well though the majority of my business is achieved through referral and word of mouth so most people will soon realise that my personality and work are very much intertwined and the reason they hire me for a job.

Industry/Entity Type

Business

Font styles to use
Other font styles liked:
• Eurostile or similar

Requirements
Must have
• I have a very open mind when it comes to design. I do like the existing tag line but if you can come up with something better I'm all ears! (and eyes)

Nice to have
• Back of the business card can be graphics, there can be transparent elements or holes, embossing options...
Should not have
• Besides my name, nothing should scream "I am woman!" because in my industry that's not a selling point.

The colour pink is a definite no.

```html
<!DOCTYPE html>
<html lang="en">
<head>
<meta charset="utf-8">
<title>Gleam Nova — Business Card</title>
<link href="https://fonts.googleapis.com/css2?family=Montserrat:wght@300&family=Open+Sans:ital,wght@0,700;1,400;1,600&display=swap" rel="stylesheet">
<style>
  :root {
    --page: #ffffff;
    --band: #231f20;
    --band-glow: #3a3637;
    --sky: #29abe2;
    --text-light: #ffffff;
    --text-muted: #c9c9c9;
  }
  html, body {
    margin: 0;
    width: 1200px;
    height: 1000px;
    overflow: hidden;
    background: var(--page);
  }
  .card {
    position: absolute;
    left: 385px;
    width: 428px;
    height: 246px;
    box-shadow: 0 18px 40px rgba(0,0,0,0.28);
    overflow: hidden;
  }
  .card--front { top: 199px; }
  .card--back  { top: 524px; }
  .card svg { position: absolute; inset: 0; display: block; }

  .brand-name {
    position: absolute;
    left: 164px;
    top: 148px;
    margin: 0;
    font-family: "Montserrat", sans-serif;
    font-weight: 300;
    font-size: 38px;
    letter-spacing: 0.5px;
    color: var(--text-light);
  }

  .roles {
    position: absolute;
    left: 21px;
    top: 162px;
    margin: 0;
    padding: 0;
    list-style: none;
    font-family: "Open Sans", sans-serif;
    font-weight: 700;
    font-size: 11px;
    line-height: 15px;
    letter-spacing: 1.6px;
    color: var(--text-light);
  }

  .contact {
    position: absolute;
    right: 20px;
    top: 123px;
    text-align: right;
    font-family: "Open Sans", sans-serif;
    color: var(--text-light);
    letter-spacing: 1.2px;
  }
  .contact__name {
    margin: 0;
    font-weight: 700;
    font-size: 14px;
    line-height: 19px;
    letter-spacing: 1.6px;
  }
  .contact__line {
    margin: 0;
    font-style: italic;
    font-weight: 400;
    font-size: 13px;
    line-height: 17px;
  }
  .contact__line--muted { color: var(--text-muted); }
</style>
</head>
<body>

<section class="card card--front" aria-label="Card front">
  <svg viewBox="0 0 428 246" width="428" height="246">
    <defs>
      <linearGradient id="skyFront" x1="0" x2="1" y1="0" y2="0">
        <stop offset="0" stop-color="var(--sky)"/>
        <stop offset="0.6" stop-color="#ffffff"/>
      </linearGradient>
      <linearGradient id="barsTones" x1="0" x2="1" y1="0" y2="0">
        <stop offset="0" stop-color="#8a4fa3"/>
        <stop offset="0.2" stop-color="#ef7d32"/>
        <stop offset="0.4" stop-color="#e9e23b"/>
        <stop offset="0.55" stop-color="#3db36b"/>
        <stop offset="0.75" stop-color="#2a9fd8"/>
        <stop offset="1" stop-color="#e5323f"/>
      </linearGradient>
      <linearGradient id="bandFront" x1="0" x2="1" y1="0" y2="0">
        <stop offset="0" stop-color="var(--band)"/>
        <stop offset="0.4" stop-color="var(--band-glow)"/>
        <stop offset="1" stop-color="var(--band)"/>
      </linearGradient>
    </defs>
    <rect width="428" height="246" fill="url(#skyFront)"/>
    <rect role="img" aria-label="Skyline of colourful rising bars" x="0" y="45" width="428" height="201" fill="url(#barsTones)" opacity="0.85"/>
    <path class="band" d="M0 72 C120 110 220 140 300 138 C360 137 400 132 428 130 L428 246 C330 215 230 200 150 207 C90 212 40 225 0 235 Z" fill="url(#bandFront)"/>
  </svg>
  <h1 class="brand-name">gleam nova</h1>
</section>

<section class="card card--back" aria-label="Card back">
  <svg viewBox="0 0 428 246" width="428" height="246">
    <defs>
      <linearGradient id="skyBack" x1="0" x2="1" y1="0" y2="0">
        <stop offset="0.35" stop-color="#ffffff"/>
        <stop offset="1" stop-color="var(--sky)"/>
      </linearGradient>
      <linearGradient id="barsTonesBack" x1="0" x2="1" y1="0" y2="0">
        <stop offset="0" stop-color="#e5323f"/>
        <stop offset="0.25" stop-color="#3db36b"/>
        <stop offset="0.45" stop-color="#ef7d32"/>
        <stop offset="0.65" stop-color="#2a9fd8"/>
        <stop offset="0.85" stop-color="#e9e23b"/>
        <stop offset="1" stop-color="#8a4fa3"/>
      </linearGradient>
      <linearGradient id="bandBack" x1="0" x2="1" y1="0" y2="0">
        <stop offset="0" stop-color="var(--band)"/>
        <stop offset="0.6" stop-color="var(--band-glow)"/>
        <stop offset="1" stop-color="var(--band)"/>
      </linearGradient>
    </defs>
    <rect width="428" height="246" fill="url(#skyBack)"/>
    <rect role="img" aria-label="Skyline of colourful rising bars" x="0" y="40" width="428" height="206" fill="url(#barsTonesBack)" opacity="0.85"/>
    <path class="band" d="M0 132 C120 136 220 128 300 112 C360 100 400 84 428 71 L428 233 C360 218 280 206 190 208 C110 210 50 228 0 246 Z" fill="url(#bandBack)"/>
  </svg>
  <ul class="roles">
    <li>Producer</li>
    <li>Editor</li>
    <li>Thinker</li>
  </ul>
  <div class="contact">
    <p class="contact__name">Petra Vandoren</p>
    <p class="contact__line">[M] +61 492 157 630</p>
    <p class="contact__line contact__line--muted">[E] pv@brightpanel.com.au</p>
    <p class="contact__line contact__line--muted">www.brightpanel.com.au</p>
  </div>
</section>

</body>
</html>
```